Tech start-up (innovation, industry 4.0, cloud computing) needs a web design+html/css

Company name: Zelmark Technologies

Hi, I need a web design for a tech start-up.

It needs to be mobile, tablet, laptop and monitor friendly

It should contain:
-Logo (in file uploads)
-A header / welcome section, including a language switcher for english and french (I will do the translations myself)
-List of services/products offered
Custom software development
Cloud computing expertise
Consulting
Turn-key solutions

-Fields of expertise
Industry 4.0
Internet of Things (IoT) + Industrial IoT
Automation
Smart manufacturing
Cloud computing
Supply chain integration
Digital twins
-Team
1 member for now
Placeholder photo
Role (President)
Bio (lorem)
Pellorin icon
My GVX certification badge (in file uploads)
Any other field you think is good to have
-Contact form (First name, last name, email, company, subject, i'm not a robot)
-Blog section
-Footer with usual stuff, pellorin icon

I want the design to inspire professionnalism, reliability, excellence but also innovation, invention, creation and dreams of a better future

Inspiration: think about smart factories, robotics, artificial intelligence, cloud computing, high-tech, the future, culture of innovation

If you could make the html+css website that would be great (no wordpress)

```html
<!DOCTYPE html>
<html lang="en">
<head>
<meta charset="utf-8">
<title>Zelmark Technologies</title>
<link href="https://fonts.googleapis.com/css2?family=Poppins:ital,wght@0,300;0,400;0,500;0,600;1,300&display=swap" rel="stylesheet">
<style>
:root{
  --navy:#0a3566;
  --navy-deep:#082a52;
  --blue:#1d6fc2;
  --blue-light:#2b86d8;
  --ink:#0c2d57;
  --orange:#f7941d;
  --muted:#7d8ea3;
  --white:#ffffff;
  --pale:#f1f6fa;
  --ring:#eef5fa;
}
*{margin:0;padding:0;box-sizing:border-box}
html,body{width:1200px;height:3866px;overflow:hidden}
body{position:relative;font-family:'Poppins',sans-serif;color:var(--ink);background:var(--white)}
.abs{position:absolute}
.hero-bg{position:absolute;left:0;top:0;width:1200px;height:1040px}
/* nav */
.brand{left:162px;top:24px;font-size:24px;font-weight:500;color:var(--white);display:flex;align-items:center;gap:10px}
.brand .dot{width:30px;height:30px;border:2px solid var(--white);border-radius:50%}
.nav{left:338px;top:34px;display:flex;gap:28px;font-size:11px;color:var(--white)}
.btn-contact{left:803px;top:25px;width:134px;height:31px;border:1px solid rgba(255,255,255,.6);color:var(--white);font-size:11px;display:flex;align-items:center;justify-content:center;letter-spacing:.5px}
.btn-lang{left:950px;top:25px;width:87px;height:31px;background:var(--orange);color:var(--white);font-size:11px;display:flex;align-items:center;justify-content:center;gap:12px}
.hero-title{left:163px;top:164px;font-size:68px;line-height:76px;font-weight:600;color:var(--white)}
.hero-sub{left:164px;top:336px;font-size:20px;font-weight:300;color:#d6e4f3}
.hero-art{left:735px;top:112px;width:310px;height:318px;border-radius:10px;background:linear-gradient(160deg,#3fa2e8,#2a6fb8 60%,#e88a1d)}
/* services */
.h2{font-size:32px;font-weight:600;text-align:center;width:1200px;left:0}
.services-title{top:606px;color:var(--white)}
.service{top:676px;width:220px;text-align:center;color:var(--white)}
.service .icon{width:40px;height:40px;margin:0 auto 20px}
.service h3{font-size:17px;font-weight:500;line-height:21px;margin-bottom:18px}
.service p{font-size:10.5px;line-height:20px;color:#a9c0da;padding:0 6px}
.vline{top:684px;width:1px;height:200px;background:rgba(255,255,255,.18)}
/* expertise */
.expertise-title{top:1092px;color:var(--ink)}
.field h4{font-size:15px;font-weight:600;line-height:18px;color:var(--ink)}
.field .bar{width:28px;height:2px;background:var(--blue);margin:8px 0 12px}
.field p{font-size:10.5px;line-height:18px;color:var(--muted)}
.field.left{text-align:right;width:240px;left:103px}
.field.left .bar{margin-left:auto}
.field.right{width:200px;left:841px}
.ficon{width:52px;height:52px;border-radius:50%;background:var(--white);box-shadow:0 2px 8px rgba(12,45,87,.15);display:flex;align-items:center;justify-content:center}
/* team */
.team-title{top:1818px;color:var(--ink)}
.team-photo{left:242px;top:1907px;width:191px;height:186px;background:linear-gradient(135deg,#c9a57c,#7f8e97 55%,#3b4651)}
.team-name{left:235px;top:2104px;font-size:13px;color:var(--orange)}
.team-name span{color:var(--blue);font-size:11px;margin-left:8px}
.social{left:421px;top:2104px;width:19px;height:19px;border-radius:50%;background:var(--blue)}
.badge-label{left:495px;top:1910px;font-size:12px;color:var(--muted)}
.badge-line{left:650px;top:1919px;width:135px;height:1px;background:#e1e7ee}
.bio{left:495px;top:1948px;width:385px;font-size:10.5px;line-height:20.5px;color:var(--muted)}
.btn-more{left:497px;top:2093px;width:87px;height:30px;background:var(--orange);color:var(--white);font-size:10.5px;display:flex;align-items:center;justify-content:center;box-shadow:0 3px 8px rgba(247,148,29,.35)}
.testi-label{left:0;width:1200px;top:2183px;text-align:center;font-size:10.5px;font-weight:600;letter-spacing:2.5px}
.quote{left:270px;width:660px;top:2227px;text-align:center;font-size:19px;line-height:31.5px;font-style:italic;font-weight:300;color:#4e5f78}
.arrow{width:38px;height:38px;border-radius:50%;display:flex;align-items:center;justify-content:center}
/* blog */
.blog-bg{left:0;top:2467px;width:1200px;height:603px;background:var(--pale)}
.blog-title{top:2536px;color:var(--ink)}
.card{top:2608px;width:275px;height:302px;background:var(--white);box-shadow:0 2px 10px rgba(12,45,87,.08);padding:12px}
.card .thumb{height:175px}
.card h5{font-size:14px;font-weight:500;line-height:19.5px;color:var(--ink);margin-top:20px;padding:0 2px}
.btn-all{left:547px;top:2940px;width:106px;height:32px;border:1px solid #d8c2a6;color:var(--orange);font-size:10.5px;display:flex;align-items:center;justify-content:center;background:var(--white)}
/* contact */
.contact-photo{left:0;top:3070px;width:1200px;height:530px;background:linear-gradient(120deg,#d9dde2,#a7acb2 45%,#6c6258 80%,#c9ccd0)}
.contact-card{left:193px;top:3157px;width:344px;height:483px;background:var(--white);box-shadow:0 6px 20px rgba(0,0,0,.15)}
.contact-head{height:55px;background:var(--blue);color:var(--white);font-size:25px;font-weight:500;text-align:center;line-height:55px}
.input{left:24px;width:296px;height:44px;border:1px solid #e1e3e6;background:#f7f8f9;font-size:9px;color:#555;padding:14px 12px}
.input.active{border:2px solid var(--orange);background:var(--white)}
.robot{left:24px;top:400px;width:125px;height:31px;border:1px solid #d6d6d6;background:#f9f9f9;font-size:6px;display:flex;align-items:center;gap:6px;padding-left:6px;color:#444}
.robot i{width:11px;height:11px;border:1px solid #bbb;background:var(--white)}
.btn-submit{left:193px;top:400px;width:127px;height:28px;background:var(--orange);color:var(--white);font-size:10px;display:flex;align-items:center;justify-content:center}
/* footer */
.footer{left:0;top:3600px;width:1200px;height:266px;background:var(--navy-deep)}
.f-text{font-size:9.5px;line-height:14px;color:#c8d6e6}
.f-links{left:447px;top:3711px;font-size:9.5px;color:#c8d6e6;line-height:25px}
.f-sub-title{left:569px;top:3710px;font-size:14px;color:var(--white)}
.f-input{left:569px;top:3775px;width:146px;height:27px;border-bottom:1px solid #3a5d86;font-size:8.5px;color:#9fb3ca;padding:8px 12px}
.f-btn{left:718px;top:3775px;width:83px;height:29px;background:var(--orange);color:var(--white);font-size:9.5px;display:flex;align-items:center;justify-content:center}
.f-brand{left:805px;top:3708px;font-size:28px;font-weight:500;color:var(--orange);display:flex;align-items:center;gap:10px}
.f-brand .dot{width:30px;height:30px;border-radius:50%;border:2px solid var(--orange)}
.f-copy{left:830px;top:3790px;width:160px;text-align:center;font-size:9px;line-height:13px;color:#c8d6e6}
</style>
</head>
<body>

<svg class="hero-bg" viewBox="0 0 1200 1040" aria-hidden="true">
  <defs>
    <linearGradient id="heroGrad" x1="0" y1="0" x2="0.3" y2="1">
      <stop offset="0" stop-color="#0b3566"/>
      <stop offset="1" stop-color="#0f4f8f"/>
    </linearGradient>
    <linearGradient id="bandGrad" x1="0" y1="0" x2="1" y2="0">
      <stop offset="0" stop-color="#1e70c4"/>
      <stop offset="1" stop-color="#1a64b5"/>
    </linearGradient>
    <clipPath id="heroClip"><path d="M0 0H1200V908Q600 1168 0 895Z"/></clipPath>
  </defs>
  <g clip-path="url(#heroClip)">
    <rect width="1200" height="1040" fill="url(#heroGrad)"/>
    <rect x="0" y="-125" width="1100" height="250" rx="125" fill="url(#bandGrad)" transform="translate(690,418) rotate(-38)"/>
  </g>
</svg>

<div class="abs brand"><span class="dot"></span>Zelmark</div>
<nav class="abs nav"><span>Products</span><span>Cloud Services</span><span>About Us</span></nav>
<div class="abs btn-contact">CONTACT US</div>
<div class="abs btn-lang">ENG
  <svg width="9" height="6" viewBox="0 0 9 6"><path d="M1 1l3.5 3.5L8 1" stroke="#fff" stroke-width="1.4" fill="none"/></svg>
</div>

<h1 class="abs hero-title">Zelmark<br>Technologies</h1>
<p class="abs hero-sub">Creation And Dreams Of A Better Future</p>
<div class="abs hero-art" role="img" aria-label="Isometric illustration of a cloud data centre with server towers and technicians"></div>

<h2 class="abs h2 services-title">Services</h2>
<div class="abs vline" style="left:395px"></div>
<div class="abs vline" style="left:618px"></div>
<div class="abs vline" style="left:825px"></div>

<div class="abs service" style="left:159px">
  <svg class="icon" viewBox="0 0 40 40" fill="none" stroke="#fff" stroke-width="1.5"><rect x="8" y="20" width="24" height="14" rx="2"/><circle cx="20" cy="12" r="6"/><path d="M4 36h32"/></svg>
  <h3>Custom software<br>development</h3>
  <p>Lorem ipsum dolor sit amet, consectetuer adipiscing elit, sed diam nonummy nibh euismod tincidunt ut laoreet dolore magna aliquam erat volutpat.</p>
</div>
<div class="abs service" style="left:397px">
  <svg class="icon" viewBox="0 0 40 40" fill="none" stroke="#fff" stroke-width="1.5"><rect x="6" y="10" width="28" height="24" rx="3"/><circle cx="14" cy="22" r="3"/><circle cx="20" cy="22" r="3"/><circle cx="26" cy="22" r="3"/></svg>
  <h3>Cloud computing<br>expertise</h3>
  <p>Ut wisi enim ad minim veniam, quis nostrud exerci tation ullamcorper suscipit lobortis nisl ut aliquip ex ea commodo consequat.</p>
</div>
<div class="abs service" style="left:611px">
  <svg class="icon" viewBox="0 0 40 40" fill="none" stroke="#fff" stroke-width="1.5"><rect x="8" y="26" width="24" height="8"/><circle cx="20" cy="16" r="5"/><rect x="24" y="4" width="12" height="9"/></svg>
  <h3>Consulting</h3>
  <p>Duis autem vel eum iriure dolor in hendrerit in vulputate velit esse molestie consequat, vel illum dolore eu feugiat nulla facilisis at</p>
</div>
<div class="abs service" style="left:832px">
  <svg class="icon" viewBox="0 0 40 40" fill="none" stroke="#fff" stroke-width="1.5"><circle cx="22" cy="14" r="9"/><path d="M18 24v6h8v-6"/><circle cx="9" cy="12" r="4"/></svg>
  <h3>Consulting</h3>
  <p>Lorem ipsum dolor sit amet, consectetuer adipiscing elit, sed diam nonummy nibh euismod tincidunt ut laoreet dolore magna aliquam erat volutpat.</p>
</div>

<h2 class="abs h2 expertise-title">Fields Of Expertise</h2>

<svg class="abs" style="left:0;top:1150px" width="1200" height="640" viewBox="0 1150 1200 640" aria-hidden="true">
  <circle cx="600" cy="1555" r="187" fill="var(--ring)"/>
  <circle cx="600" cy="1555" r="155" fill="#f8fbfd"/>
  <g stroke="#9cc1de" stroke-width="1" stroke-dasharray="3 3" fill="none">
    <path d="M603 1335V1430"/>
    <path d="M413 1386H475L532 1444"/>
    <path d="M779 1386H718L660 1444"/>
    <path d="M413 1530H470"/>
    <path d="M779 1530H722"/>
    <path d="M413 1693H472L515 1650"/>
    <path d="M779 1693H720L677 1650"/>
  </g>
</svg>

<div class="abs field" style="left:500px;top:1180px;width:206px;text-align:center">
  <h4>Industry 4.0</h4>
  <div class="bar" style="margin:8px auto 12px"></div>
  <p>Lorem ipsum dolor sit amet, consectetuer adipiscing elit, sed diam nonummy nibh</p>
</div>
<div class="abs ficon" style="left:577px;top:1282px"><svg width="26" height="26" viewBox="0 0 26 26" fill="none" stroke="#f7941d" stroke-width="1.4"><path d="M4 22h18M8 22V12l5-6 5 6v10"/></svg></div>

<div class="abs field left" style="top:1366px"><h4>Internet of Things (IoT)<br>+ Industrial IoT</h4><div class="bar"></div><p>Lorem ipsum dolor sit amet,<br>consectetuer adipiscing elit, sed<br>diam nonummy nibh</p></div>
<div class="abs ficon" style="left:360px;top:1360px"><svg width="26" height="26" viewBox="0 0 26 26" fill="none" stroke="#f7941d" stroke-width="1.4"><circle cx="13" cy="13" r="9"/><circle cx="13" cy="13" r="3"/></svg></div>

<div class="abs field left" style="top:1510px"><h4>Automation</h4><div class="bar"></div><p>Aliquam erat volutpat. Ut wisi<br>enim ad minim veniam, quis<br>nostrud exerci tation</p></div>
<div class="abs ficon" style="left:360px;top:1504px"><svg width="26" height="26" viewBox="0 0 26 26" fill="none" stroke="#f7941d" stroke-width="1.4"><rect x="7" y="5" width="12" height="9"/><path d="M9 14v7h8v-7"/></svg></div>

<div class="abs field left" style="top:1673px"><h4>Smart manufacturing</h4><div class="bar"></div><p>Duis autem vel eum iriure dolor in<br>hendrerit in vulputate velit esse<br>molestie consequat,</p></div>
<div class="abs ficon" style="left:360px;top:1667px"><svg width="26" height="26" viewBox="0 0 26 26" fill="none" stroke="#f7941d" stroke-width="1.4"><path d="M4 22h18M6 22v-8h14v8M10 14V6h6"/></svg></div>

<div class="abs field right" style="top:1366px"><h4>Cloud computing</h4><div class="bar"></div><p>Duis autem vel eum iriure dolor in<br>hendrerit in vulputate velit esse<br>molestie consequat,</p></div>
<div class="abs ficon" style="left:780px;top:1360px"><svg width="26" height="26" viewBox="0 0 26 26" fill="none" stroke="#f7941d" stroke-width="1.4"><path d="M7 18a4 4 0 0 1 0-8 6 6 0 0 1 11 1 3.5 3.5 0 0 1 0 7z"/></svg></div>

<div class="abs field right" style="top:1510px"><h4>Supply chain<br>integration</h4><div class="bar"></div><p>&nbsp;Lorem ipsum dolor sit amet,<br>consectetuer adipiscing elit, sed diam<br>nonummy nibh</p></div>
<div class="abs ficon" style="left:780px;top:1504px"><svg width="26" height="26" viewBox="0 0 26 26" fill="none" stroke="#f7941d" stroke-width="1.4"><circle cx="13" cy="13" r="9"/><circle cx="13" cy="13" r="5"/></svg></div>

<div class="abs field right" style="top:1673px"><h4>Digital twins</h4><div class="bar"></div><p>Aliquam erat volutpat. Ut wisi<br>enim ad minim veniam, quis<br>nostrud exerci tation</p></div>
<div class="abs ficon" style="left:780px;top:1667px"><svg width="26" height="26" viewBox="0 0 26 26" fill="none" stroke="#f7941d" stroke-width="1.4"><circle cx="13" cy="13" r="5"/><path d="M13 3v4M13 19v4M3 13h4M19 13h4"/></svg></div>

<h2 class="abs h2 team-title">Our Team</h2>
<div class="abs team-photo" role="img" aria-label="Placeholder portrait of the company president at his desk"></div>
<div class="abs team-name">Dorian<span>( President )</span></div>
<div class="abs social" aria-label="Pellorin profile"></div>
<div class="abs badge-label">GVX certification badge</div>
<div class="abs badge-line"></div>
<svg class="abs" style="left:786px;top:1893px" width="50" height="54" viewBox="0 0 50 54" aria-label="Certification badge"><path d="M25 2l22 12.5v25L25 52 3 39.5v-25z" fill="#2d3fb0"/></svg>
<p class="abs bio">Lorem ipsum dolor sit amet, consectetuer adipiscing elit, sed diam nonummy nibh euismod tincidunt ut laoreet dolore magna aliquam erat volutpat. Ut wisi enim ad minim veniam, quis nostrud exerci tation ullamcorper suscipit lobortis nisl ut aliquip ex ea commodo consequat. Duis autem vel eum iriure dolor in hendrerit in vulputate velit esse molestie consequat, vel illum dolore eu feugiat nulla facilisis at vero eros et</p>
<div class="abs btn-more">Read More</div>

<div class="abs testi-label">Testimonial</div>
<p class="abs quote">Lorem ipsum dolor sit amet, consectetuer adipiscing elit, sed diam nonummy nibh euismod tincidunt ut laoreet dolore magna aliquam erat volutpat. Ut wisi enim ad minim veniam, quis nostrud exerci tation ullamcorper suscipit lobortis nisl ut aliquip ex ea commodo consequat. Duis autem vel eum iriure dolor in hendrerit in vulputate velit esse molestie consequat, vel illum dolore eu feugiat nulla facilisis at vero eros et</p>
<div class="abs arrow" style="left:163px;top:2304px;border:1px solid #dde3ea"><svg width="12" height="10" viewBox="0 0 12 10"><path d="M11 5H1M5 1L1 5l4 4" stroke="#c3ccd6" fill="none" stroke-width="1.2"/></svg></div>
<div class="abs arrow" style="left:999px;top:2304px;border:2px solid var(--blue)"><svg width="12" height="10" viewBox="0 0 12 10"><path d="M1 5h10M7 1l4 4-4 4" stroke="#1d6fc2" fill="none" stroke-width="1.4"/></svg></div>

<div class="abs blog-bg"></div>
<h2 class="abs h2 blog-title">Blog</h2>
<article class="abs card" style="left:162px"><div class="thumb" role="img" aria-label="Team meeting around an office table" style="background:linear-gradient(135deg,#e3e5e4,#9aa39f 55%,#5b5e5a)"></div><h5>Lorem ipsum dolor sit amet, consectetuer adipiscing elit, sed diam nonummy nibh</h5></article>
<article class="abs card" style="left:462px"><div class="thumb" role="img" aria-label="Hand touching a glowing digital interface" style="background:linear-gradient(135deg,#0b2a3a,#1a7a8e 55%,#0a1e2c)"></div><h5>Duis autem vel eum iriure dolor in hendrerit in vulputate</h5></article>
<article class="abs card" style="left:762px"><div class="thumb" role="img" aria-label="Laptop keyboard with floating security icons" style="background:linear-gradient(135deg,#d7dde2,#6c7a86 55%,#27313b)"></div><h5>Ut wisi enim ad minim veniam, quis nostrud exerci tation ullamcorper suscipit lobortis nisl ut aliquip ex ea commodo consequat.</h5></article>
<div class="abs btn-all">View All News</div>

<div class="abs contact-photo" role="img" aria-label="Top view of colleagues working with laptops around a meeting table"></div>
<form class="abs contact-card">
  <div class="contact-head">Contact Us</div>
  <div class="abs input active" style="top:86px">First name*</div>
  <div class="abs input" style="top:143px">last name*</div>
  <div class="abs input" style="top:201px">email*</div>
  <div class="abs input" style="top:260px">company*</div>
  <div class="abs input" style="top:318px;height:68px">subject*</div>
  <div class="abs robot"><i></i>I'm not a robot</div>
  <div class="abs btn-submit">Submit</div>
</form>

<footer class="abs footer"></footer>
<svg class="abs" style="left:207px;top:3712px" width="11" height="14" viewBox="0 0 11 14"><path d="M5.5 13S1 8 1 5a4.5 4.5 0 0 1 9 0c0 3-4.5 8-4.5 8z" fill="none" stroke="#f7941d" stroke-width="1.3"/><circle cx="5.5" cy="5" r="1.5" fill="#f7941d"/></svg>
<p class="abs f-text" style="left:229px;top:3711px;width:160px">Halvern House, 14 Marlow Reach, Brisford, BR7 2QX, United Kingdom</p>
<svg class="abs" style="left:207px;top:3778px" width="12" height="12" viewBox="0 0 12 12"><path d="M2 1h3l1 3-1.5 1a7 7 0 0 0 2.5 2.5L8 6l3 1v3a1 1 0 0 1-1 1A9 9 0 0 1 1 2a1 1 0 0 1 1-1z" fill="none" stroke="#f7941d" stroke-width="1.2"/></svg>
<p class="abs f-text" style="left:229px;top:3777px">555-014-2298</p>
<svg class="abs" style="left:207px;top:3810px" width="12" height="10" viewBox="0 0 12 10"><rect x="0.6" y="0.6" width="10.8" height="8.8" fill="none" stroke="#f7941d" stroke-width="1.2"/><path d="M1 1l5 4 5-4" fill="none" stroke="#f7941d" stroke-width="1.2"/></svg>
<p class="abs f-text" style="left:229px;top:3808px">info@zelmarktech.example</p>
<div class="abs f-links">Home<br>IT Support<br>Cloud services<br>About Us<br>Contact</div>
<div class="abs f-sub-title">Subscribe to Latest News</div>
<p class="abs f-text" style="left:569px;top:3744px;font-size:8px">Latest news and promotions delivered to your inbox!</p>
<div class="abs f-input">Enter Your Email</div>
<div class="abs f-btn">SUBSCRIBE</div>
<div class="abs f-brand"><span class="dot"></span>Zelmark</div>
<p class="abs f-copy">©2022 zelmarktech -<br>All Rights Reserved.</p>

</body>
</html>
```